Marlow Crest Homes Needs Business Card Design

Looking for a unique modern business card to fit my new Logo.
Name: Dean Marlow
Company: Marlow Crest Homes, LLC
Tag Line: Forever Framed Right
Email: marlowcresthomes@mailvista.test
Phone: (253) 555-0187
Website: www.marlowcresthomes.test
License: MARLOCH462QT

```html
<!DOCTYPE html>
<html lang="en">
<head>
<meta charset="utf-8">
<title>Marlow Crest Homes – Business Card</title>
<link href="https://fonts.googleapis.com/css2?family=Montserrat:wght@400;500;700;800&display=swap" rel="stylesheet">
<style>
  :root {
    --backdrop: #a3a3a3;
    --card: #141414;
    --white: #ffffff;
    --blue: #3399d0;
    --text-light: #f2f2f2;
  }
  * { margin: 0; padding: 0; box-sizing: border-box; }
  html, body {
    width: 1146px; height: 1200px; overflow: hidden;
    background: var(--backdrop);
    font-family: "Montserrat", Arial, sans-serif;
  }
  .canvas { position: relative; width: 1146px; height: 1200px; }
  .card {
    position: absolute; left: 191px; width: 768px;
    background: var(--card); overflow: hidden;
  }
  .card--front { top: 128px; height: 439px; }
  .card--back { top: 608px; height: 446px; }

  /* Front */
  .front-lockup {
    position: absolute; left: 96px; top: 160px;
    display: flex; align-items: center; gap: 26px;
  }
  .brand-square { width: 64px; height: 64px; background: var(--blue); flex: none; }
  .front-text { display: flex; flex-direction: column; }
  .tagline {
    font-weight: 500; font-size: 20px; letter-spacing: 1px;
    color: var(--white); margin-bottom: 10px;
  }
  .tagline .accent { color: var(--blue); }
  .brand-name--front {
    font-weight: 800; font-size: 44px; line-height: 1; color: var(--white);
    letter-spacing: -0.5px;
  }

  /* Back */
  .back-lockup {
    position: absolute; left: 33px; top: 40px;
    display: flex; align-items: center; gap: 16px;
  }
  .brand-square--small { width: 40px; height: 40px; }
  .brand-name--back {
    font-weight: 800; font-size: 28px; line-height: 1; color: var(--white);
  }
  .person-name {
    position: absolute; left: 30px; top: 196px;
    font-weight: 700; font-size: 36px; letter-spacing: 0.5px; color: var(--blue);
  }
  .contact-list {
    position: absolute; left: 32px; top: 276px; list-style: none;
    font-size: 21px; color: var(--text-light);
  }
  .contact-list li {
    display: flex; align-items: center; gap: 8px; height: 34px;
  }
  .contact-list svg { width: 20px; height: 20px; flex: none; }
  .contact-list .license { margin-top: 6px; padding-left: 2px; }
</style>
</head>
<body>
<main class="canvas">
  <section class="card card--front">
    <div class="front-lockup">
      <span class="brand-square" aria-hidden="true"></span>
      <div class="front-text">
        <p class="tagline">FOREVER <span class="accent">FRAMED</span> RIGHT</p>
        <h1 class="brand-name--front">MARLOW CREST HOMES</h1>
      </div>
    </div>
  </section>

  <section class="card card--back">
    <div class="back-lockup">
      <span class="brand-square brand-square--small" aria-hidden="true"></span>
      <p class="brand-name--back">MARLOW CREST HOMES</p>
    </div>
    <h2 class="person-name">DEAN MARLOW</h2>
    <ul class="contact-list">
      <li>
        <svg viewBox="0 0 20 20" aria-hidden="true"><path fill="var(--blue)" d="M2 7c0-3 4-4 8-4s8 1 8 4v1h-4V6H6v2H2zM4 9h12l1 8H3z"/></svg>
        (253) 555-0187
      </li>
      <li>
        <svg viewBox="0 0 20 20" aria-hidden="true"><rect x="1" y="4" width="18" height="12" fill="var(--blue)"/><path d="M1 4l9 7 9-7" fill="none" stroke="var(--card)" stroke-width="1.5"/></svg>
        marlowcresthomes@mailvista.test
      </li>
      <li>
        <svg viewBox="0 0 20 20" aria-hidden="true"><circle cx="10" cy="10" r="9" fill="var(--blue)"/><path d="M1 10h18M10 1c-4 4-4 14 0 18M10 1c4 4 4 14 0 18" fill="none" stroke="var(--card)" stroke-width="1"/></svg>
        www.marlowcresthomes.test
      </li>
      <li class="license">License: MARLOCH462QT</li>
    </ul>
  </section>
</main>
</body>
</html>
```